Design A Responsive Website for Our Bar/Event Center and Restaurant

We need a Responsive Word Press Website for our Bar Event Center and our Restaurant. We need 5 pages with one page being our menu with the ability for customers to place online orders for food.
We need the entire website designed, coded and deployed. We have domain names already that need to link to the website and we also have hosting so we need the website deployed at our hosting provider. Pages should include 1) About Us 2)Bar 3)Restaurant-Menus 4) Event Venue-With Calendar 5) Contact Us

Target Market(s)

Adults 21-75 in the Louisville KY area, that go to bars, night clubs, concerts and karaoke events

Industry/Entity Type

Bar-Night Club-Music- Events

Coding

Coded - Design and coding required

Number of Pages Required

5+ page

Other font styles liked:
• Use a Font like in our logos

Colors
EE7325
F08F49
F5BC92
FAE3D3
FDF4ED
EB3D1F
EC4F4E
F09395
F8D3D4
FCEDEE

Requirements
Must have
• Online Menu Ordering with Shopping Cart, An Updateable Event Calendar, A page for posting past event pictures and videos, Ability to sell Event tickets
Nice to have
• Ability to live stream events to facebook
Should not have
• NA

```html
<!DOCTYPE html>
<html lang="en">
<head>
<meta charset="utf-8">
<title>Ember Wing House – Restaurant</title>
<link rel="stylesheet" href="https://fonts.googleapis.com/css2?family=Poppins:wght@400;500;600;700;800&family=Roboto:wght@400;500&display=swap">
<style>
:root{
  --orange:#EE7325;
  --orange-mid:#F08F49;
  --orange-soft:#F5BC92;
  --orange-pale:#FAE3D3;
  --ink:#474659;
  --text:#6b6b6b;
  --white:#ffffff;
  --line:#d9d9d9;
}
*{margin:0;padding:0;box-sizing:border-box}
html,body{width:1200px;height:3793px;overflow:hidden;background:var(--white)}
body{position:relative;font-family:'Roboto',Arial,sans-serif;color:var(--text)}
.abs{position:absolute}
.brand{font-family:'Poppins',sans-serif;font-weight:700;font-size:22px;color:var(--orange);display:flex;align-items:center;gap:8px;white-space:nowrap}
.brand-dot{width:14px;height:14px;border-radius:50%;background:var(--orange)}

/* hero */
.hero{left:0;top:0;width:1200px;height:545px;background:radial-gradient(ellipse at 50% 45%,#6b4a2e 0%,#3a2718 45%,#1c130d 100%)}
.topbar{left:0;top:0;width:1200px;height:15px;background:#1b1b1b}
.header-brand{left:177px;top:42px;height:34px}
.nav-links{top:48px;font-family:'Poppins',sans-serif;font-size:15px;color:#fff;white-space:nowrap}
.nav-links span{position:absolute;top:0}
.nav-links .active{color:var(--orange)}
.nav-links .active::after{content:"";position:absolute;left:10%;right:10%;bottom:-8px;height:4px;border-bottom:2px solid var(--orange);border-radius:50%}
.cart{left:899px;top:43px;width:32px;height:32px;border-radius:50%;background:#fff;display:flex;align-items:center;justify-content:center}
.signup{left:964px;top:51px;font-family:'Poppins',sans-serif;font-size:13px;color:var(--orange);display:flex;gap:4px;align-items:center;white-space:nowrap}
.crumb{left:174px;top:175px;font-family:'Poppins',sans-serif;font-size:13px;color:#fff;white-space:nowrap}
.hero-title{left:0;width:1200px;top:228px;text-align:center;font-family:'Poppins',sans-serif;font-weight:700;font-size:40px;color:#fff}

/* welcome */
.plate-ring{left:128px;top:705px;width:405px;height:445px;border:1.5px solid var(--orange-soft);border-radius:48% 52% 45% 55%/50% 45% 55% 50%;transform:rotate(-8deg)}
.plate{left:140px;top:735px;width:382px;height:382px;border-radius:50%;background:radial-gradient(circle at 45% 40%,#fbf8f5 0%,#f1ece7 60%,#e4ded8 100%);box-shadow:0 8px 20px rgba(0,0,0,.1)}
.kicker{left:593px;top:688px;font-family:'Poppins',sans-serif;font-weight:800;font-size:14px;color:var(--orange);font-style:italic}
.welcome-title{left:593px;top:718px;width:440px;font-family:'Poppins',sans-serif;font-weight:600;font-size:37px;line-height:53px;color:var(--ink)}
.welcome-copy{left:593px;top:830px;width:435px;font-size:13.6px;line-height:24.3px;color:var(--text)}

/* banner */
.banner{left:0;top:1229px;width:1200px;height:461px;background:radial-gradient(ellipse at 50% 50%,#2e2a28 0%,#3b2a24 40%,#4a2f25 70%,#2a1d18 100%)}
.banner-title{left:0;width:1200px;top:1335px;text-align:center;font-family:'Poppins',sans-serif;font-weight:800;font-size:54px;line-height:72px;color:#fff}
.banner-copy{left:300px;width:600px;top:1480px;text-align:center;font-family:'Poppins',sans-serif;font-size:14px;line-height:21px;color:#fff}
.btn{display:flex;align-items:center;justify-content:center;background:var(--orange-mid);color:#fff;font-family:'Poppins',sans-serif;font-size:13px;border-radius:22px;white-space:nowrap}
.order-btn{left:524px;top:1553px;width:153px;height:33px}

/* menu */
.section-title{left:0;width:1200px;text-align:center;font-family:'Poppins',sans-serif;font-weight:500;font-size:36px;color:var(--ink)}
.card{width:274px;height:334px;background:#fff;border-radius:10px;box-shadow:0 4px 14px rgba(0,0,0,.08);overflow:hidden}
.card-img{width:274px;height:216px;border-radius:10px}
.stars{position:absolute;left:24px;top:232px;color:var(--orange-mid);font-size:13px;letter-spacing:6px}
.card-name{position:absolute;left:24px;top:259px;font-family:'Poppins',sans-serif;font-size:16px;color:var(--ink);white-space:nowrap}
.add-btn{position:absolute;left:24px;top:294px;width:80px;height:20px;border:1px solid var(--orange-soft);background:var(--orange-pale);color:var(--orange-mid);font-size:9px;display:flex;align-items:center;justify-content:center;border-radius:3px;font-family:'Poppins',sans-serif;white-space:nowrap}
.price{position:absolute;right:24px;top:298px;font-size:10px;color:var(--orange-mid);font-family:'Poppins',sans-serif}
.view-btn{left:489px;top:2691px;width:224px;height:44px}

/* reservation */
.reserve{left:0;top:2841px;width:1200px;height:515px;background:radial-gradient(ellipse at 25% 90%,#c8257a 0%,rgba(200,37,122,0) 40%),radial-gradient(ellipse at 75% 30%,#5a2db8 0%,rgba(90,45,184,0) 50%),linear-gradient(180deg,#0f1034 0%,#2a1a6a 45%,#6a1f7a 80%,#3a1660 100%)}
.reserve-title{left:0;width:1200px;top:2928px;text-align:center;font-family:'Poppins',sans-serif;font-weight:700;font-size:36px;color:#fff}
.reserve-copy{left:340px;width:560px;top:2988px;text-align:center;font-family:'Poppins',sans-serif;font-size:13px;line-height:21px;color:#fff}
.field{height:44px;background:#fff;border-radius:22px;display:flex;align-items:center;padding:0 20px;font-family:'Poppins',sans-serif;font-size:13px;color:#888;gap:14px;white-space:nowrap}
.field .grow{flex:1}
.agree{left:685px;top:3137px;display:flex;gap:14px;align-items:flex-start;font-size:13px;color:#fff;font-weight:500;line-height:16px;white-space:nowrap}
.agree .box{width:17px;height:17px;background:#fff;margin-top:4px;flex:none}
.find-btn{left:506px;top:3205px;width:224px;height:44px}

/* footer */
.foot-logo{left:174px;top:3522px}
.foot-nav{top:3530px;font-family:'Poppins',sans-serif;font-size:15px;color:#777;white-space:nowrap}
.foot-nav span{position:absolute;top:0}
.rule{left:174px;width:852px;height:1px;background:var(--line)}
.contact{top:3633px;display:flex;align-items:center;gap:14px;font-size:13px;color:#333;font-weight:500;white-space:nowrap}
.contact .ic{width:36px;height:36px;border-radius:50%;background:var(--orange-mid);display:flex;align-items:center;justify-content:center}
.socials{left:859px;top:3634px;display:flex;gap:10px}
.socials span{width:34px;height:34px;border-radius:50%;background:var(--orange-mid)}
.copyright{left:0;width:1200px;top:3742px;text-align:center;font-size:14px;color:#999}
</style>
</head>
<body>

<!-- hero -->
<div class="abs hero" role="img" aria-label="Close-up of a burger with fries on a wooden board"></div>
<div class="abs topbar"></div>
<svg class="abs" style="left:0;top:505px" width="1200" height="42" viewBox="0 0 1200 42" preserveAspectRatio="none">
  <path d="M0 30 C120 12 220 40 360 22 C470 8 560 42 700 30 C820 20 900 2 1020 18 C1100 28 1160 14 1200 10 L1200 42 L0 42Z" fill="#fff"/>
</svg>
<div class="abs brand header-brand"><span class="brand-dot"></span>Ember Wing House</div>
<nav class="abs nav-links" style="left:0">
  <span style="left:461px">Home</span>
  <span style="left:523px">About</span>
  <span style="left:589px">Bar</span>
  <span class="active" style="left:630px">Restaurant</span>
  <span style="left:730px">Events</span>
  <span style="left:796px">Contact</span>
</nav>
<div class="abs cart"><svg width="14" height="14" viewBox="0 0 24 24"><path d="M3 4h3l2.5 11h10L21 7H7" fill="none" stroke="#EE7325" stroke-width="2.5"/><circle cx="9" cy="19" r="2" fill="#EE7325"/><circle cx="17" cy="19" r="2" fill="#EE7325"/></svg></div>
<div class="abs signup"><svg width="11" height="11" viewBox="0 0 24 24"><circle cx="12" cy="7" r="5" fill="#EE7325"/><path d="M2 23c0-6 5-9 10-9s10 3 10 9z" fill="#EE7325"/></svg>Sign Up</div>
<div class="abs crumb">Home &nbsp;&rsaquo;&nbsp; Resturant</div>
<h1 class="abs hero-title">Restaurant</h1>

<!-- welcome -->
<div class="abs plate-ring"></div>
<div class="abs plate" role="img" aria-label="Plated salmon dish with lemon and asparagus"></div>
<div class="abs kicker">WELCOME!</div>
<h2 class="abs welcome-title">Enjoy An Exceptional Journey of Taste</h2>
<p class="abs welcome-copy">Lorem ipsum dolor sit amet, consectetur adipiscing elit, sed do eiusmod tempor incididunt ut labore et dolore magna aliqua. Ut enim ad minim veniam, quis nostrud exercitation ullamco laboris nisi ut aliquip ex ea commodo consequat. Duis aute irure dolor in reprehenderit in voluptate velit esse cillum dolore eu fugiat nulla pariatur. Excepteur sint occaecat cupidatat non proident, sunt in culpa qui officia deserunt mollit anim id est laborum.<br>\ed ut perspiciatis unde omnis iste natus error sit voluptatem accusantium doloremque laudantium, totam rem aperiam, eaque ipsa quae ab illo inventore veritatis et quasi architecto beatae vitae dicta sunt explicabo. Nemo enim ipsam voluptatem quia voluptas sit</p>

<!-- banner -->
<div class="abs banner" role="img" aria-label="Overhead spread of hot dishes, sushi and grilled meat"></div>
<svg class="abs" style="left:0;top:1222px" width="1200" height="30" viewBox="0 0 1200 30" preserveAspectRatio="none">
  <path d="M0 0 L1200 0 L1200 10 C1120 0 1060 2 1000 14 C900 30 780 6 660 10 C540 14 480 28 380 14 C280 2 160 26 0 18Z" fill="#fff"/>
</svg>
<svg class="abs" style="left:0;top:1662px" width="1200" height="30" viewBox="0 0 1200 30" preserveAspectRatio="none">
  <path d="M0 10 C140 20 260 2 400 14 C520 24 600 6 720 12 C860 20 980 2 1080 14 C1140 20 1180 14 1200 12 L1200 30 L0 30Z" fill="#fff"/>
</svg>
<h2 class="abs banner-title">THE REAL TASTE OF<br>HOT FOOD!</h2>
<p class="abs banner-copy">Lorem ipsum dolor sit amet, consectetur adipiscing elit, sed do eiusmod tempor incididunt ut labore et dolore magna aliqua. Ut enim ad minim veniam, quis nostrud</p>
<div class="abs btn order-btn">ORDER NOW</div>

<!-- menu -->
<h2 class="abs section-title" style="top:1806px">Restaurant Menus</h2>

<article class="abs card" style="left:174px;top:1914px">
  <div class="card-img" role="img" aria-label="Burger with fries" style="background:linear-gradient(160deg,#3a4a2a,#8a5a2a 60%,#c9a060)"></div>
  <div class="stars">★★★★★</div><div class="card-name">Burgerers</div>
  <div class="add-btn">ADD TO CART</div><div class="price">$25.00</div>
</article>
<article class="abs card" style="left:462px;top:1914px">
  <div class="card-img" role="img" aria-label="Breaded steak with fries and salad" style="background:linear-gradient(160deg,#7a6a5a,#c88a3a 55%,#e0c070)"></div>
  <div class="stars">★★★★★</div><div class="card-name">Steak or Chicken &amp; Fries</div>
  <div class="add-btn">ADD TO CART</div><div class="price">$25.00</div>
</article>
<article class="abs card" style="left:751px;top:1914px">
  <div class="card-img" role="img" aria-label="Meatball sub with chips" style="background:linear-gradient(160deg,#c9a070,#b04a2a 55%,#e8d8b8)"></div>
  <div class="stars">★★★★★</div><div class="card-name">Meatball Sub &amp; Chips</div>
  <div class="add-btn">ADD TO CART</div><div class="price">$25.00</div>
</article>

<article class="abs card" style="left:174px;top:2289px">
  <div class="card-img" role="img" aria-label="Chicken bacon ranch skillet" style="background:linear-gradient(160deg,#8a3a1a,#d8a040 55%,#5a2a1a)"></div>
  <div class="stars">★★★★★</div><div class="card-name">Chicken Bacon Ranch</div>
  <div class="add-btn">ADD TO CART</div><div class="price">$25.00</div>
</article>
<article class="abs card" style="left:462px;top:2289px">
  <div class="card-img" role="img" aria-label="Glazed chicken wings with dip" style="background:linear-gradient(160deg,#2a2c30,#6a2e18 55%,#1e2226)"></div>
  <div class="stars">★★★★★</div><div class="card-name">Chicken Wings</div>
  <div class="add-btn">ADD TO CART</div><div class="price">$25.00</div>
</article>
<article class="abs card" style="left:751px;top:2289px">
  <div class="card-img" role="img" aria-label="Bratwurst burger with tater tots" style="background:linear-gradient(180deg,#a01818,#7a1010 45%,#c8902a 75%,#6a6a6a)"></div>
  <div class="stars">★★★★★</div><div class="card-name">Tow Brats &amp; Tate Tots</div>
  <div class="add-btn">ADD TO CART</div><div class="price">$25.00</div>
</article>

<div class="abs btn view-btn">VIEW MORE</div>

<!-- reservation -->
<div class="abs reserve" role="img" aria-label="Purple and pink stage lights background"></div>
<svg class="abs" style="left:0;top:2836px" width="1200" height="30" viewBox="0 0 1200 30" preserveAspectRatio="none">
  <path d="M0 0 L1200 0 L1200 6 C1120 14 1060 2 980 10 C880 20 800 4 700 8 C580 14 520 26 400 12 C300 2 180 24 0 14Z" fill="#fff"/>
</svg>
<svg class="abs" style="left:0;top:3328px" width="1200" height="32" viewBox="0 0 1200 32" preserveAspectRatio="none">
  <path d="M0 12 C120 22 240 4 380 14 C500 22 600 4 740 12 C880 22 980 4 1100 16 C1150 20 1180 14 1200 10 L1200 32 L0 32Z" fill="#fff"/>
</svg>
<h2 class="abs reserve-title">Make A Reservation</h2>
<p class="abs reserve-copy">Lorem ipsum dolor sit amet, consectetur adipiscing elit, sed do eiusmod tempor incididunt ut labore et dolore magna aliqua.</p>

<div class="abs field" style="left:278px;top:3062px;width:221px">
  <svg width="13" height="13" viewBox="0 0 24 24"><circle cx="12" cy="7" r="5" fill="none" stroke="#EE7325" stroke-width="2"/><path d="M3 22c0-5 4-8 9-8s9 3 9 8" fill="none" stroke="#EE7325" stroke-width="2"/></svg>
  <span class="grow">2 Person</span>
  <svg width="12" height="8" viewBox="0 0 12 8"><path d="M1 1l5 5 5-5" fill="none" stroke="#EE7325" stroke-width="1.5"/></svg>
</div>
<div class="abs field" style="left:506px;top:3062px;width:223px">
  <span class="grow">dd-mm-yyyy</span>
  <svg width="12" height="12" viewBox="0 0 24 24"><rect x="2" y="4" width="20" height="18" rx="2" fill="#EE7325"/></svg>
</div>
<div class="abs field" style="left:736px;top:3062px;width:222px">
  <svg width="13" height="13" viewBox="0 0 24 24"><circle cx="12" cy="12" r="10" fill="#EE7325"/><path d="M12 6v6l4 2" stroke="#fff" stroke-width="2" fill="none"/></svg>
  <span class="grow">04:00 pm</span>
  <svg width="12" height="8" viewBox="0 0 12 8"><path d="M1 1l5 5 5-5" fill="none" stroke="#EE7325" stroke-width="1.5"/></svg>
</div>
<div class="abs field" style="left:278px;top:3125px;width:355px">
  <svg width="13" height="13" viewBox="0 0 24 24"><path d="M6 2l4 4-2 3c1 3 4 6 7 7l3-2 4 4-3 4C10 22 2 14 2 5z" fill="#EE7325"/></svg>
  <span class="grow">Phone</span>
</div>
<label class="abs agree"><span class="box"></span><span>I agree that my submitted data is being<br>collected and stored.</span></label>
<div class="abs btn find-btn">FIND A TICKET</div>

<!-- footer -->
<div class="abs brand foot-logo">Ember Wing House</div>
<nav class="abs foot-nav" style="left:0">
  <span style="left:529px">Home</span>
  <span style="left:612px">About</span>
  <span style="left:694px">Bar</span>
  <span style="left:756px">Restaurant</span>
  <span style="left:872px">Event</span>
  <span style="left:958px">Contact</span>
</nav>
<div class="abs rule" style="top:3582px"></div>

<div class="abs contact" style="left:174px">
  <span class="ic"><svg width="14" height="16" viewBox="0 0 24 28"><path d="M12 0a10 10 0 0 1 10 10c0 8-10 18-10 18S2 18 2 10A10 10 0 0 1 12 0z" fill="#fff"/><circle cx="12" cy="10" r="4" fill="#F08F49"/></svg></span>
  1280 Harbor Lane Riverton
</div>
<div class="abs contact" style="left:456px">
  <span class="ic"><svg width="15" height="15" viewBox="0 0 24 24"><path d="M6 2l4 4-2 3c1 3 4 6 7 7l3-2 4 4-3 4C10 22 2 14 2 5z" fill="#fff"/></svg></span>
  25-555-0142
</div>
<div class="abs contact" style="left:622px">
  <span class="ic"><svg width="16" height="12" viewBox="0 0 24 18"><rect x="1" y="1" width="22" height="16" rx="2" fill="#fff"/><path d="M2 3l10 7 10-7" fill="none" stroke="#F08F49" stroke-width="2"/></svg></span>
  hello@emberwing.com
</div>
<div class="abs socials"><span></span><span></span><span></span><span></span></div>
<div class="abs rule" style="top:3717px"></div>
<p class="abs copyright">© 2022 Ember Wing House All right reserve</p>

</body>
</html>
```